Poster Design Needed for Events

I would like a poster designed for our events.. We do evenings of Mediumship/Psychic at theatres ect.. the image below would need to be included... I Would also like the following wording to be included... "Renowned Spiritualist Medium Dafydd Pemberton Presents Whispers From the Lighthouse" There will also Need to be a Place on the poster where event details can be put.. as they Change everytime.. Colours for background maybe blue,, maybe Clouds ect..

```html
<!DOCTYPE html>
<html lang="en">
<head>
<meta charset="utf-8">
<title>Whispers From the Lighthouse – Event Poster</title>
<link rel="stylesheet" href="https://fonts.googleapis.com/css2?family=Roboto:wght@300;400;700;900&display=swap">
<style>
  :root {
    --ink-white: #ffffff;
    --name-yellow: #fff200;
    --title-cyan: #3bb6c9;
    --detail-gold: #e6cf63;
    --band-red: #7a1c12;
    --band-orange: #b5561c;
    --band-amber: #b88a24;
    --band-yellow: #a79a2c;
    --band-green: #5b6f2a;
    --band-teal: #1f3d3e;
    --band-navy: #101c2a;
    --night: #060606;
  }
  * { box-sizing: border-box; margin: 0; padding: 0; }
  html, body { width: 1200px; height: 750px; overflow: hidden; background: var(--night); }
  .poster {
    position: relative;
    width: 1200px;
    height: 750px;
    overflow: hidden;
    font-family: "Roboto", Arial, sans-serif;
    color: var(--ink-white);
    background:
      linear-gradient(to bottom,
        var(--band-red) 0px, var(--band-red) 70px,
        #a0321a 78px, #a0321a 148px,
        var(--band-orange) 156px, var(--band-orange) 228px,
        var(--band-amber) 236px, var(--band-amber) 300px,
        var(--band-yellow) 308px, var(--band-yellow) 372px,
        #7f8430 380px, #7f8430 448px,
        var(--band-green) 456px, var(--band-green) 522px,
        var(--band-teal) 530px, var(--band-teal) 590px,
        var(--band-navy) 600px, var(--night) 650px);
  }
  .poster__shade {
    position: absolute; inset: 0;
    background:
      radial-gradient(ellipse 70% 75% at 55% 40%, rgba(0,0,0,0) 0%, rgba(0,0,0,0.55) 100%),
      linear-gradient(to right, rgba(0,0,0,0.45) 0%, rgba(0,0,0,0.1) 45%, rgba(0,0,0,0.35) 100%);
  }
  .poster__ghost-portrait {
    position: absolute; left: 500px; top: 20px; width: 340px; height: 630px;
    border-radius: 170px 170px 40px 40px;
    background: radial-gradient(ellipse at 50% 40%, rgba(255,220,170,0.22), rgba(0,0,0,0) 70%);
  }
  .poster__host-portrait {
    position: absolute; left: 790px; top: 40px; width: 410px; height: 710px;
    border-radius: 180px 160px 0 0;
    background: linear-gradient(to bottom, #3a2a2a 0%, #1d1a24 45%, #0c0c14 100%);
  }
  .headline { position: absolute; left: 55px; top: 62px; }
  .headline__intro {
    font-weight: 300; font-size: 62px; line-height: 82px; letter-spacing: 0.5px;
    text-transform: uppercase;
  }
  .headline__name {
    font-weight: 900; font-size: 50px; line-height: 66px; margin-top: 4px;
    color: var(--name-yellow); text-transform: uppercase; letter-spacing: 1px;
  }
  .headline__presents {
    font-weight: 300; font-size: 60px; line-height: 78px; letter-spacing: 0.36em;
    text-transform: uppercase;
  }
  .headline__title {
    font-weight: 900; font-size: 62px; line-height: 78px; letter-spacing: -1.5px;
    color: var(--title-cyan); text-transform: uppercase; margin-top: 2px;
  }
  .details { position: absolute; top: 655px; left: 0; width: 700px; height: 90px; }
  .details__item { position: absolute; top: 0; text-align: center; transform: translateX(-50%); }
  .details__item--venue { left: 183px; width: 300px; }
  .details__item--date { left: 418px; width: 140px; }
  .details__item--time { left: 580px; width: 160px; }
  .details__label { font-weight: 300; font-size: 23px; letter-spacing: 1px; line-height: 28px; }
  .details__value { color: var(--detail-gold); font-size: 12.5px; line-height: 18px; margin-top: 12px; }
</style>
</head>
<body>
  <main class="poster">
    <div class="poster__ghost-portrait" role="img" aria-label="Faint large portrait of the medium blended into the background"></div>
    <div class="poster__shade"></div>
    <div class="poster__host-portrait" role="img" aria-label="Photo of the medium in a dark suit, reaching toward the viewer"></div>

    <header class="headline">
      <p class="headline__intro">Renowned<br>Spiritualist<br>Medium</p>
      <p class="headline__name">Dafydd Pemberton</p>
      <p class="headline__presents">Presents</p>
      <h1 class="headline__title">Whispers From<br>The Lighthouse</h1>
    </header>

    <section class="details">
      <div class="details__item details__item--venue">
        <p class="details__label">VENUE</p>
        <p class="details__value">#154, Lorem Ipsum is simply dummy<br>text of the printing and 1542512 industry. 56452</p>
      </div>
      <div class="details__item details__item--date">
        <p class="details__label">DATE</p>
        <p class="details__value">21 . 02 . 216</p>
      </div>
      <div class="details__item details__item--time">
        <p class="details__label">TIME</p>
        <p class="details__value">10 Am to 1PM</p>
      </div>
    </section>
  </main>
</body>
</html>
```